Vardell Therapeutics is a biotech company that needs a powerpoint theme.

We need a powerpoint theme with several different slide templates we could use for presentation of data or research ideas. Our logo is attached. We picked "Vardell" as our company name because we use epigenome editing tools to fine-tune gene expression for therapeutic purposes. Our logo color is a seafoam green, and we would like to see this color along with other colors that could complement it well. Keywords: genetics, biotech, cells, human therapies,

```html
<!DOCTYPE html>
<html lang="en">
<head>
<meta charset="utf-8">
<title>Vardell Therapeutics – Content Slide</title>
<link rel="stylesheet" href="https://fonts.googleapis.com/css2?family=Open+Sans:wght@400;600&family=Carlito:wght@400;700&display=swap">
<style>
  :root {
    --slide-bg: #f6f6f6;
    --seafoam: #1a9c8c;
    --seafoam-bright: #00cdb6;
    --ocean: #0a7fb0;
    --coral: #ff8a73;
    --cream: #f8f6dc;
    --ink-dark: #333544;
    --body-text: #5a5a5a;
    --white: #ffffff;
  }
  * { margin: 0; padding: 0; box-sizing: border-box; }
  html, body { width: 1200px; height: 675px; overflow: hidden; background: var(--slide-bg); }
  .slide {
    position: relative;
    width: 1200px; height: 675px;
    background: var(--slide-bg);
    font-family: "Open Sans", sans-serif;
    overflow: hidden;
  }
  .slide-title {
    position: absolute; left: 91px; top: 44px;
    font-size: 33px; font-weight: 400;
    color: var(--seafoam);
  }
  .title-rule {
    position: absolute; left: 75px; top: 95px;
    width: 1050px; height: 3px;
    background: var(--seafoam);
  }
  .body-copy {
    position: absolute; left: 92px; top: 186px;
    width: 440px;
    font-size: 18.3px; line-height: 27.3px;
    color: var(--body-text);
  }
  .chart-panel {
    position: absolute; left: 643px; top: 157px;
    width: 482px; height: 377px;
    background: var(--ink-dark);
    border-radius: 36px;
    box-shadow: 0 2px 6px rgba(0,0,0,0.35);
    font-family: "Carlito", sans-serif;
  }
  .chart-title {
    position: absolute; top: 12px; width: 100%;
    text-align: center;
    font-size: 23px; font-weight: 700;
    color: var(--white);
  }
  .pie { position: absolute; left: 103px; top: 56px; }
  .legend {
    position: absolute; top: 350px; width: 100%;
    display: flex; justify-content: center; gap: 14px;
    font-size: 13px; color: var(--white);
  }
  .legend-item { display: flex; align-items: center; gap: 4px; }
  .swatch { width: 8px; height: 8px; display: inline-block; }
  .footer-band { position: absolute; left: 0; top: 520px; }
  .brand {
    position: absolute; left: 203px; top: 612px;
    display: flex; align-items: center; gap: 14px;
  }
  .brand-dot {
    width: 38px; height: 38px; border-radius: 50%;
    border: 4px solid var(--seafoam-bright);
  }
  .brand-name {
    font-size: 20px; font-weight: 400; letter-spacing: 3px;
    color: var(--white); text-transform: uppercase;
  }
  .page-number {
    position: absolute; right: 48px; top: 628px;
    font-size: 26px; color: var(--white);
    font-family: "Open Sans", sans-serif;
  }
</style>
</head>
<body>
<main class="slide">
  <h1 class="slide-title">Title 1</h1>
  <div class="title-rule"></div>

  <p class="body-copy">We need a powerpoint theme with several different slide templates we could use for presentation of data or research ideas. Our logo is attached. We picked "Vardell" as our company name because we use epigenome editing tools to fine-tune gene expression for therapeutic purposes. Our logo color is a seafoam green, and we would like to see this color along with other colors that could complement it well. Keywords: genetics, biotech, cells, human therapies,</p>

  <section class="chart-panel">
    <div class="chart-title">Sales</div>
    <svg class="pie" width="274" height="274" viewBox="-137 -137 274 274">
      <path d="M0 0 L0 -137 A137 137 0 1 1 -70.6 117.4 Z" fill="var(--seafoam-bright)"/>
      <path d="M0 0 L-70.6 117.4 A137 137 0 0 1 -126.1 -53.5 Z" fill="var(--ocean)"/>
      <path d="M0 0 L-126.1 -53.5 A137 137 0 0 1 -70.6 -117.4 Z" fill="var(--coral)"/>
      <path d="M0 0 L-70.6 -117.4 A137 137 0 0 1 0 -137 Z" fill="var(--cream)"/>
    </svg>
    <div class="legend">
      <span class="legend-item"><i class="swatch" style="background:var(--seafoam-bright)"></i>1st Qtr</span>
      <span class="legend-item"><i class="swatch" style="background:var(--ocean)"></i>2nd Qtr</span>
      <span class="legend-item"><i class="swatch" style="background:var(--coral)"></i>3rd Qtr</span>
      <span class="legend-item"><i class="swatch" style="background:var(--cream)"></i>4th Qtr</span>
    </div>
  </section>

  <svg class="footer-band" width="1200" height="155" viewBox="0 520 1200 155">
    <path d="M0 625 C150 602 350 575 550 604 S900 660 1200 560 L1200 675 L0 675 Z" fill="var(--ink-dark)"/>
    <g role="img" aria-label="DNA double-helix strands running along the wave">
      <path d="M0 622 C150 598 320 560 520 578 S850 610 1000 640" fill="none" stroke="var(--seafoam-bright)" stroke-width="6" stroke-opacity="0.55"/>
      <path d="M420 590 C600 610 800 660 1000 645 S1150 600 1200 548" fill="none" stroke="var(--seafoam-bright)" stroke-width="6" stroke-opacity="0.55"/>
    </g>
  </svg>

  <div class="brand">
    <span class="brand-dot"></span>
    <span class="brand-name">Vardell Therapeutics</span>
  </div>
  <div class="page-number">17</div>
</main>
</body>
</html>
```